"Moss Under Stone Taxidermy" is the name of business.

Birds and Small Mammals are the focus. Coyotes, Foxes, Beavers, Ducks, Birds etc.,
Nassology
Preserving the natural beauty of animals through moss under stone.

I would like the logo to include a style of images/symbols in this tattoo and of this buzzard drawing. Not quite hieroglyphic but similar style. Preferred vertically arranged

Art
After on one side
Death
Taxidermy

Snake
Moon on other side
Buzzard

```html
<!DOCTYPE html>
<html lang="en">
<head>
<meta charset="utf-8">
<title>Moss Under Stone Taxidermy – Business Card</title>
<link rel="stylesheet" href="https://fonts.googleapis.com/css2?family=Cinzel:wght@700&display=swap">
<style>
  :root {
    --backdrop: #676767;
    --card: #ffffff;
    --gold: #ae8348;
  }
  html, body {
    margin: 0;
    padding: 0;
    width: 1200px;
    height: 1200px;
    overflow: hidden;
    background: var(--backdrop);
  }
  .canvas {
    position: relative;
    width: 1200px;
    height: 1200px;
    background: var(--backdrop);
  }
  .card {
    position: absolute;
    left: 174px;
    width: 850px;
    height: 472px;
    background: var(--card);
  }
  .card--front { top: 94px; }
  .card--back { top: 634px; }

  .brand-mark {
    position: absolute;
    left: 50%;
    top: 153px;
    width: 80px;
    height: 80px;
    margin-left: -40px;
    border: 3px solid var(--gold);
    border-radius: 50%;
    box-sizing: border-box;
  }
  .brand-name {
    position: absolute;
    left: 0;
    right: 0;
    top: 326px;
    margin: 0;
    text-align: center;
    font-family: "Cinzel", serif;
    font-weight: 700;
    font-size: 24px;
    letter-spacing: 0.5px;
    color: var(--gold);
    line-height: 1;
  }
  .brand-sub {
    position: absolute;
    left: 0;
    right: 0;
    top: 376px;
    margin: 0;
    text-align: center;
    font-family: "Cinzel", serif;
    font-weight: 700;
    font-size: 11px;
    line-height: 1;
    letter-spacing: 9px;
    padding-left: 9px;
    text-transform: uppercase;
    color: var(--gold);
  }
  .brand-sub::before,
  .brand-sub::after {
    content: "\25C6";
    font-size: 6px;
    vertical-align: middle;
    margin: 0 8px;
    letter-spacing: 0;
  }

  .frame {
    position: absolute;
    left: 0;
    top: 0;
    width: 850px;
    height: 472px;
  }
  .back-text {
    position: absolute;
    left: 0;
    right: 0;
    margin: 0;
    text-align: center;
    font-family: "Cinzel", serif;
    font-weight: 700;
    color: var(--gold);
    line-height: 1;
    letter-spacing: 0.5px;
  }
  .specialty {
    top: 92px;
    font-size: 22px;
    line-height: 30px;
  }
  .owner { top: 234px; font-size: 24px; }
  .location { top: 318px; font-size: 24px; }
  .phone { top: 359px; font-size: 25px; }

  .divider {
    position: absolute;
    left: 363px;
    width: 124px;
    height: 16px;
  }
  .divider--upper { top: 200px; }
  .divider--lower { top: 270px; }
  .divider .rule {
    position: absolute;
    top: 7px;
    width: 41px;
    height: 2px;
    background: var(--gold);
  }
  .divider .rule--left { left: 0; }
  .divider .rule--right { right: 0; }
  .divider .ornament {
    position: absolute;
    left: 55px;
    top: 1px;
    width: 14px;
    height: 14px;
    border-radius: 50%;
    background: var(--gold);
  }
</style>
</head>
<body>
<div class="canvas">
  <section class="card card--front">
    <div class="brand-mark"></div>
    <h1 class="brand-name">Moss Under Stone</h1>
    <p class="brand-sub">Taxidermy</p>
  </section>

  <section class="card card--back">
    <svg class="frame" viewBox="0 0 850 472" aria-hidden="true">
      <path d="M70 40 H758 A29 29 0 0 0 787 69 V427 A29 29 0 0 0 758 456 H70 A29 29 0 0 0 41 427 V69 A29 29 0 0 0 70 40 Z"
            fill="none" stroke="#ae8348" stroke-width="2.5"/>
    </svg>
    <p class="back-text specialty">Specializing in birds,<br>waterfowl and small<br>mammals</p>
    <div class="divider divider--upper">
      <span class="rule rule--left"></span>
      <span class="ornament" role="img" aria-label="Small crescent ornament"></span>
      <span class="rule rule--right"></span>
    </div>
    <p class="back-text owner">Wren Callaway</p>
    <div class="divider divider--lower">
      <span class="rule rule--left"></span>
      <span class="ornament" role="img" aria-label="Small moon ornament"></span>
      <span class="rule rule--right"></span>
    </div>
    <p class="back-text location">Fernhollow, SC</p>
    <p class="back-text phone">803-555-0147</p>
  </section>
</div>
</body>
</html>
```